Posters for Sociology/Inequality exhibition

I need about 10 similarly themed A2 sized posters (so you don't need to do each one from scratch) for a Sociology exhibition on Inequality. The first half are general descriptions about Sociology, the second half, about inequality. They are meant to be educational to a university student audience.

We are from the Lantern Society. I have attached a file below about the write-up content for the various posters, do have a look and do your sample base on that. The write-up is not yet complete, so it may change. Likewise, the point form of the write-up are for reading only, I don't expect them to be in the poster.

Feel free to separate the points if you find them too wordy, because I do not have an idea how the poster will eventually look like. Try your best!

-

Note: There were some problems with the word file attached, but I have changed and fixed it already, do have a look at it!

Also, I need the posters by Saturday/Sunday so most probably I will award the winner before that. I need it done earlier than later because I still need to get it approved.

The size may be big but that's because I want it to be readable, rather than have too many things in it.

You don't have to do all the 10 different ones first, just start with some or a few, submit a sample, and we'll take it from there!

Please ask if you have any questions!

Hi everyone, post your samples (1 or a few) soon because I will have a make a decision soon, most probably by tomorrow. 

I know it's rushed but try your best.

Target Market(s)

18-28 years old students at an institute/university

Industry/Entity Type

University

Requirements
Must have
• 1. A consistent theme that runs throughout the posters.
2. Very Readable, Appealing Font
3. Visually appealing for an exhibition
Should not have
• Not be too overwhelming

```html
<!DOCTYPE html>
<html lang="en">
<head>
<meta charset="utf-8">
<title>What Is Sociology? — Lantern Society</title>
<link rel="stylesheet" href="https://fonts.googleapis.com/css2?family=Bebas+Neue&family=Open+Sans:ital,wght@1,600;1,700&display=swap">
<style>
  :root {
    --ink: #000000;
    --crimson: #c10f2a;
    --crimson-deep: #8c0b21;
    --crimson-shade: #a20d26;
    --cream: #f6e7cb;
    --paper: #ffffff;
  }
  * { margin: 0; padding: 0; box-sizing: border-box; }
  html, body { width: 927px; height: 1200px; overflow: hidden; background: var(--ink); }
  .poster {
    position: relative;
    width: 927px;
    height: 1200px;
    background: var(--ink);
    font-family: "Bebas Neue", "Oswald", sans-serif;
    color: var(--ink);
    overflow: hidden;
  }
  .headline {
    position: absolute;
    color: var(--crimson);
    line-height: 0.9;
    white-space: nowrap;
    font-weight: 400;
  }
  .headline--intro { left: 46px; top: 44px; font-size: 112px; letter-spacing: 1px; }
  .headline--practice { left: 44px; top: 472px; font-size: 82px; z-index: 2; }

  .panel { position: absolute; left: 45px; width: 838px; background: var(--crimson); }
  .panel--definition { top: 145px; height: 303px; }
  .panel--methods { top: 538px; height: 613px; overflow: hidden; }

  .figures {
    position: absolute;
    left: 402px; top: 38px;
    width: 436px; height: 575px;
    background: linear-gradient(180deg, var(--crimson-shade) 0%, var(--crimson-deep) 45%, var(--crimson-deep) 100%);
  }

  .line { position: absolute; white-space: nowrap; line-height: 1; }
  .line--lead { left: 102px; top: 32px; font-size: 48px; color: var(--cream); }
  .line--body { left: 26px; font-size: 37px; }
  .line--note { left: 72px; top: 212px; font-size: 33px; color: var(--cream); }
  .line--italic {
    font-family: "Open Sans", "Helvetica Neue", sans-serif;
    font-style: italic;
    font-weight: 600;
    color: var(--paper);
    letter-spacing: 2.4px;
  }
  .line--note-italic { left: 41px; top: 252px; font-size: 25px; }

  .methods-text { position: relative; z-index: 1; }
  .methods-text .line { left: 26px; }
  .line--m { font-size: 29px; }
  .line--q { font-size: 35px; }
  .line--scale { left: 58px !important; top: 291px; font-size: 19px; letter-spacing: 2.2px; }
  .line--micro { top: 336px; font-size: 41px; }

  .study-label {
    position: absolute;
    left: 45px; top: 951px;
    width: 394px; height: 122px;
    background: var(--ink);
    color: var(--crimson);
    z-index: 3;
    padding: 0 0 0 2px;
  }
  .study-label .big { display: block; font-size: 88px; line-height: 0.82; margin-top: -2px; }
  .study-label .small { display: block; font-size: 47px; line-height: 0.9; }

  .study-list {
    position: absolute;
    left: 452px; top: 944px;
    width: 430px;
    font-family: "Open Sans", "Helvetica Neue", sans-serif;
    font-style: italic;
    font-weight: 600;
    font-size: 19.5px;
    line-height: 1.3;
    letter-spacing: 1.6px;
    color: var(--paper);
    z-index: 3;
  }
</style>
</head>
<body>
<main class="poster">
  <h1 class="headline headline--intro">What Is Sociology?</h1>

  <section class="panel panel--definition">
    <p class="line line--lead">Sociology is the study of society.</p>
    <p class="line line--body" style="top:96px">It is a social science involving the study of the social</p>
    <p class="line line--body" style="top:141px">lives of people, groups, and societies.</p>
    <p class="line line--note">An overarching unification of all the studies of humankind,</p>
    <p class="line line--italic line--note-italic">including History, Psychology, and Economics.</p>
  </section>

  <h2 class="headline headline--practice">What Do Sociologists Do?</h2>

  <section class="panel panel--methods">
    <div class="figures" role="img" aria-label="Abstract stylised figures of people in deep red"></div>
    <div class="methods-text">
      <p class="line line--m" style="top:17px">Sociologists use a mixture of quantitative and qualitative methods</p>
      <p class="line line--m" style="top:50px">to understand their areas of study.</p>
      <p class="line line--m" style="top:93px">Quantitative are a set of mathematical models or tools used to chart</p>
      <p class="line line--m" style="top:131px">certain levels of social relations with high levels of certainty.</p>
      <p class="line line--q" style="top:193px">Qualitative are the close to close, subjective</p>
      <p class="line line--q" style="top:238px">understandings of different social situations.</p>
      <p class="line line--italic line--scale">Sociologists may study it at the micro or macro levels.</p>
      <p class="line line--micro">Micro meaning, from 1 person to a group of people.</p>
    </div>
  </section>

  <h2 class="study-label"><span class="big">What Do</span><span class="small">Sociologists Study?</span></h2>
  <p class="study-list">Some areas Sociologists study include: The Family, Gender relations, Work, Race and Ethnicity, Politics, Culture, Social Change Movements, Sexuality, Death, Aging.</p>
</main>
</body>
</html>
```